We have a small 501C Non-Profit, called Youngsters Unite. The non-profit was started by my son and his friends during the Gulf Oil Spill. We would like to update the website that currently sits on Domivault.com. I'm not sure how we transfer over the domain or get them to host it with your new design. I've attached a link of the old site that we developed. We are open to any ideas regarding hosting.

We would basically like a look that is youth (teen, college age) oriented that will drive teens and donors to the site. Our goal is to get onto Plixa Drives, get grants and make major donations with little to no administration expense. We will get sponsors to pay for the administration costs. So we will be looking for sponsors to support the overhead and 100% of donor money will go to causes important to teens.

http://www.youngstersunite.org

Target Market(s)

Teenagers and Individual Sponsors. Adults that want to help teens with an important cause.

Industry/Entity Type

Non-Profit

Requirements
Must have
• We are very open to ideas. It would be good to have a:

Home-with Mission Statement and Photos or Graphics
Donate-100% of Donations Go To Causes (with Coinvo Link)
Become A Sponsor-Insert Contact Information In This Section.
How It All Got Started -with info, articles, events, video, etc. from Gulf Oil Spill, Our Founder photo.
Contact-Change phone number to 555-804-2739. Keep e-mail and mailing the same.

You can use some existing photos from current site if you would like. All the Recent Event Photos, Founder Photo, 3 people holding check photo were all taken by me so there are no rights issues with those.

YU Mission Statement:

To demonstrate to the world that Youngsters Unite about the environment, each other and world peace through fund raising and other philanthropic efforts.
Nice to have
• Youngsters Unite Logo If Possible

Photo of 3 people, holding check, from existing home page in new History Section.

Kindpaw League Story and Logo in History Section

WRX Video in History Section

Helpio4
http://www.helpio4.net/stories/youth-launches-charity-to-fund-relief-for-wildlife-harmed-by-coastal-slick.html
Should not have
• Delete Blog Section
Delete Founder Section
Delete Recent Events
Delete How To Get Involved

```html
<!DOCTYPE html>
<html lang="en">
<head>
<meta charset="utf-8">
<title>Youngsters Unite – Donate</title>
<link rel="stylesheet" href="https://fonts.googleapis.com/css2?family=Pathway+Gothic+One&family=Arimo:wght@400;700&family=PT+Sans:wght@400;700&family=Libre+Baskerville&display=swap">
<style>
:root{
  --blue:#4a6ea4;
  --nav:#3e68a8;
  --green:#8cc63f;
  --ink:#111;
  --page:#ffffff;
  --map:#eef1f6;
  --footer:#1e1e1e;
  --footer-bar:#0c0c0c;
  --footer-text:#c9c9c9;
  --partner-ink:#4a5560;
}
*{margin:0;padding:0;box-sizing:border-box}
html,body{width:1124px;height:1200px;overflow:hidden;background:var(--page)}
body{position:relative;font-family:"Arimo",Arial,sans-serif;color:var(--ink)}
.abs{position:absolute}

.map-backdrop{left:130px;top:0;width:900px;height:850px;
  background:radial-gradient(ellipse at 50% 45%,var(--map) 0%,rgba(238,241,246,.5) 50%,rgba(255,255,255,0) 75%)}

.brand{left:121px;top:34px;display:flex;align-items:center;gap:10px}
.brand-dot{width:56px;height:56px;border-radius:50%;background:var(--blue)}
.brand-name{font-family:"Libre Baskerville",serif;font-size:29px;color:#1b1b1b}

.nav{left:0;top:89px;width:1124px;height:40px}
.nav-tab{left:525px;top:0}
.nav a{position:absolute;top:13px;font-weight:700;font-size:14.5px;color:var(--nav);text-decoration:none;letter-spacing:.2px}
.nav a.active{color:#fff}

.hero{left:123px;top:121px;width:881px;height:341px}
.hero-photo{left:522px;top:155px;width:458px;height:288px;
  background:linear-gradient(180deg,#8ea7c4 0%,#c9c4b4 45%,#e6e3dc 70%,#a89f8f 100%)}
.hero-title{left:164px;top:148px;font-family:"Pathway Gothic One",sans-serif;font-size:56px;line-height:68px;font-weight:400;color:#fff;text-shadow:2px 3px 4px rgba(0,0,0,.45)}
.hero-title span{display:block}
.hero-title .l2{padding-left:18px}
.hero-caption{left:368px;top:344px;width:148px;text-align:right;font-size:10.4px;line-height:12.6px;color:#fff;text-shadow:1px 1px 1px rgba(0,0,0,.4)}
.hero-tag{left:148px;top:375px;width:206px;height:71px;background:rgba(63,90,42,.88);
  color:#e8efe0;font-weight:700;font-size:32px;line-height:71px;padding-left:23px}

.services{left:125px;top:480px;width:245px;height:297px;border:2px solid #e1e3e6;background:rgba(255,255,255,.85)}
.service{position:absolute;left:17px;width:220px;height:58px}
.service-icon{position:absolute;left:0;top:0;width:59px;height:59px;background:var(--blue)}
.service-text{position:absolute;left:68px;top:4px;font-size:9.6px;line-height:12px}
.service-text h3{font-size:11.5px;font-weight:700;color:var(--nav);margin-bottom:3px}

.tab-label{font-size:34px;color:#fff;font-weight:400}
.donate-tab{left:396px;top:476px;width:246px;height:57px}
.donate-tab .tab-label{position:absolute;left:17px;top:7px}
.supports-tab{left:396px;top:664px;width:246px;height:57px}
.supports-tab .tab-label{position:absolute;left:17px;top:4px}

.donate-copy{left:413px;top:535px;width:580px;font-size:14px;line-height:17px}
.donate-copy p+p{margin-top:14px;width:340px}

.donation-box{left:801px;top:565px;width:197px;height:99px}
.donation-inner{left:826px;top:585px;width:156px}
.donation-inner label{display:block;font-size:14px;color:#111;margin-bottom:3px}
.select{width:154px;height:17px;border:1px solid #a9a9a9;background:#fff;font-size:11px;line-height:15px;padding-left:4px;position:relative}
.select::after{content:"";position:absolute;right:5px;top:6px;border:3px solid transparent;border-top:4px solid #000}
.cart-btn{margin-top:5px;width:103px;height:22px;border-radius:11px;border:1px solid #d08a1d;
  background:linear-gradient(#ffe99a,#f7b731);font-weight:700;font-size:12px;color:#1b3a73;text-align:center;line-height:20px}

.partner{display:flex;align-items:center;gap:8px;font-size:18px;font-weight:700;color:var(--partner-ink)}
.partner-mark{width:14px;height:14px;background:var(--partner-ink)}
.partner-a{left:452px;top:772px}
.partner-b{left:640px;top:772px}

.footer{left:0;top:859px;width:1124px;height:283px;background:var(--footer);font-family:"PT Sans",sans-serif}
.footer-col{position:absolute;top:32px;width:220px}
.footer-col h4{font-size:16.5px;line-height:21px;color:#fff;font-weight:700;margin-bottom:20px}
.footer-col li{list-style:none;font-size:13.5px;line-height:28.2px;color:var(--footer-text)}

.footer-bar{left:0;top:1142px;width:1124px;height:58px;background:var(--footer-bar);font-family:"PT Sans",sans-serif}
.footer-brand{left:109px;top:9px;display:flex;align-items:center;gap:8px}
.footer-brand .brand-dot{width:40px;height:40px;background:#6c6c6c}
.footer-brand .brand-name{font-size:21px;color:#8f8f8f}
.footer-links{left:430px;top:20px;font-size:13px;color:#a9a9a9}
.footer-links span{margin:0 9px}
.copyright{left:707px;top:20px;font-size:13px;color:#a9a9a9}
.social{top:16px;width:26px;height:26px;border-radius:3px}
.social.s1{left:907px;background:#3b5ea8}
.social.s2{left:945px;background:#38a9e0}
.social.s3{left:982px;background:#f29a1b}
</style>
</head>
<body>

<div class="abs map-backdrop" role="img" aria-label="Faint world map backdrop"></div>

<header class="abs brand">
  <div class="brand-dot"></div>
  <div class="brand-name">Youngsters Unite</div>
</header>

<nav class="abs nav">
  <svg class="abs nav-tab" width="132" height="40" viewBox="0 0 132 40"><polygon points="8,0 118,0 132,40 0,40" fill="var(--blue)"/></svg>
  <a style="left:451px" href="#">HOME</a>
  <a class="active" style="left:555px" href="#">DONATE</a>
  <a style="left:668px" href="#">SPONSOR</a>
  <a style="left:781px" href="#">HISTORY</a>
  <a style="left:894px" href="#">CONTACT</a>
</nav>

<svg class="abs hero" viewBox="0 0 881 341" width="881" height="341">
  <polygon points="22,6 881,0 874,341 0,341 12,170" fill="var(--blue)"/>
  <polygon points="32,22 860,14 852,118 640,86 420,110 250,96 130,118 40,110" fill="var(--green)"/>
  <polygon points="30,180 150,168 280,186 420,175 560,192 850,178 848,320 24,328" fill="var(--green)"/>
</svg>
<div class="abs hero-photo" role="img" aria-label="Photo of three people holding a large donation check"></div>
<h1 class="abs hero-title"><span>“Helping Others</span><span class="l2">Around The World”</span></h1>
<p class="abs hero-caption">From left to right ( Dr. Alan Rusk-Bayou Shoreline Trust, Evan Hale-A Founding Director of Youngsters Unite, Carl Ostby-Owner Levee Street Bakery)</p>
<div class="abs hero-tag">Donations</div>

<aside class="abs services">
  <div class="service" style="top:15px">
    <svg class="service-icon" viewBox="0 0 59 59"><rect width="59" height="59" fill="var(--blue)"/><path d="M17 34 v-6 a12.5 12.5 0 0 1 25 0 v6" fill="none" stroke="#fff" stroke-width="3"/><rect x="14" y="30" width="7" height="11" rx="2" fill="#fff"/><rect x="38" y="30" width="7" height="11" rx="2" fill="#fff"/></svg>
    <div class="service-text"><h3>Lorem Ipsum Dolor Sit</h3>consectetur adipiscing elit.<br>Suspendisse tristique dui eu<br>massa dapibus.</div>
  </div>
  <div class="service" style="top:83px">
    <svg class="service-icon" viewBox="0 0 59 59"><rect width="59" height="59" fill="var(--blue)"/><rect x="15" y="21" width="29" height="20" fill="#fff"/><path d="M15 21 L29.5 33 L44 21" fill="none" stroke="var(--blue)" stroke-width="2"/></svg>
    <div class="service-text"><h3>Lorem Ipsum Dolor Sit</h3>consectetur adipiscing elit.<br>Suspendisse tristique dui eu<br>massa dapibus.</div>
  </div>
  <div class="service" style="top:152px">
    <svg class="service-icon" viewBox="0 0 59 59"><rect width="59" height="59" fill="var(--blue)"/><path d="M20 16 l6 0 3 9 -4 3 c2 5 5 8 9 10 l3 -4 9 3 0 6 c-14 2 -28 -12 -26 -27z" fill="#fff"/></svg>
    <div class="service-text"><h3>Lorem Ipsum Dolor Sit</h3>consectetur adipiscing elit.<br>Suspendisse tristique dui eu<br>massa dapibus.</div>
  </div>
  <div class="service" style="top:221px">
    <svg class="service-icon" viewBox="0 0 59 59"><rect width="59" height="59" fill="var(--blue)"/><circle cx="29.5" cy="27" r="12" fill="none" stroke="#fff" stroke-width="3"/><path d="M17.5 27 h24 M29.5 15 v24" stroke="#fff" stroke-width="2"/><path d="M14 40 q15 8 31 0" fill="none" stroke="#fff" stroke-width="3"/></svg>
    <div class="service-text"><h3>Lorem Ipsum Dolor Sit</h3>consectetur adipiscing elit.<br>Suspendisse tristique dui eu<br>massa dapibus.</div>
  </div>
</aside>

<div class="abs donate-tab">
  <svg class="abs" width="246" height="57" viewBox="0 0 246 57"><polygon points="0,8 241,0 246,45 4,57" fill="var(--blue)"/></svg>
  <h2 class="tab-label">Donate Today</h2>
</div>

<div class="abs donate-copy">
  <p>Support through donation is very important because lorem ipsum dolor sit amet consectetur adipiscing elit, et amet elit quid consectetur.</p>
  <p>orem ipsum dolor sit amet consectetur adipiscing elit. Suspendisse tristique dui eu massa dapibus ipsum elit.dapibus ipsum dolor sit amet adipiscing elit.</p>
</div>

<svg class="abs donation-box" width="197" height="99" viewBox="0 0 197 99"><polygon points="3,6 195,0 197,99 0,96" fill="none" stroke="var(--blue)" stroke-width="5"/></svg>
<div class="abs donation-inner">
  <label>Donation Amount</label>
  <div class="select">$10 Donation $10.00</div>
  <div class="cart-btn">Add to Cart</div>
</div>

<div class="abs supports-tab">
  <svg class="abs" width="246" height="57" viewBox="0 0 246 57"><polygon points="0,6 243,0 246,46 3,57" fill="var(--green)"/></svg>
  <h2 class="tab-label">YU Supports:</h2>
</div>

<div class="abs partner partner-a"><span class="partner-mark"></span>Lakou Vita</div>
<div class="abs partner partner-b"><span class="partner-mark"></span>Marshwing</div>

<footer class="abs footer">
  <div class="footer-col" style="left:121px"><h4>Lorem ipsum dolor sit<br>amet consectetur</h4><ul><li>Lorem ipsum dolor sit amet</li><li>ipsum dolor sit amet</li><li>sit amet dolor ipsum et quid</li><li>Amet lorem ipsum</li></ul></div>
  <div class="footer-col" style="left:356px"><h4>ipsum dolor sit amet<br>consectetur</h4><ul><li>dolor sit amet &nbsp;ipsum</li><li>Consectetur sit amet</li><li>Lorem ipsum</li></ul></div>
  <div class="footer-col" style="left:601px"><h4>dolor sit amet quid et ae<br>consectetur</h4><ul><li>Lorem dolor sit amet</li><li>Ipsum et dolor quid un fac</li><li>dolor ipsum et quid</li><li>Ipsum et dolor quid un fac</li><li>Ipsum et quid</li></ul></div>
  <div class="footer-col" style="left:846px"><h4>Lorem ipsum dolor sit<br>amet consectetur</h4><ul><li>Lorem ipsum dolor sit amet</li><li>ipsum dolor</li><li>Consectetur quid und fac</li></ul></div>
</footer>

<div class="abs footer-bar">
  <div class="abs footer-brand"><div class="brand-dot"></div><div class="brand-name">Youngsters Unite</div></div>
  <div class="abs footer-links">Privacy Policy<span>|</span>Sitemap</div>
  <div class="abs copyright">Copreight 2012</div>
  <div class="abs social s1" aria-label="Plixa"></div>
  <div class="abs social s2" aria-label="Chirply"></div>
  <div class="abs social s3" aria-label="Feed"></div>
</div>

</body>
</html>
```